Varnath Consulting Business card design.

See our website www.varnathconsulting-example.com which will give you a good idea of what we are about. The font is called 'Play'.

I'd like a standout business card in keeping with the themes and branding on the website

Target Market(s)

professionals. HR directors

Industry/Entity Type

Business

Contact Information for Business Card

Varnath Consulting PO Box 3917 Tindale Creek NSW 2840 1300 457 318 Gerald Ashbury Principal email: jobs@varnathconsulting-example.com ABN: 31792048663

Font styles to use
Other font styles liked:
• Play

Requirements
Must have
• Must have same design colours and branding as website.
• On back I'd prefer a list of the things we do which appears below the name at the header on the website

```html
<!DOCTYPE html>
<html lang="en">
<head>
<meta charset="utf-8">
<title>Varnath Consulting – Business Card</title>
<link rel="stylesheet" href="https://fonts.googleapis.com/css2?family=Play:wght@400;700&family=Arimo:wght@400;700&display=swap">
<style>
  :root {
    --stage: #e9e6e1;
    --navy-deep: #0c1d2f;
    --navy: #17304a;
    --ink: #1c2e42;
    --brand-blue: #2aa3e2;
    --muted: #8a8f95;
    --paper: #ffffff;
    --on-dark: #e8eef4;
  }
  * { box-sizing: border-box; margin: 0; padding: 0; }
  html, body {
    width: 1200px; height: 950px; overflow: hidden;
    background: var(--stage);
  }
  .canvas { position: relative; width: 1200px; height: 950px; }

  .card {
    position: absolute;
    width: 640px; height: 391px;
    border-radius: 4px;
    box-shadow: 0 10px 28px rgba(0,0,0,.18);
    overflow: hidden;
  }

  /* Back of card */
  .card--back {
    left: 120px; top: 60px;
    background: linear-gradient(135deg, var(--navy) 0%, var(--navy-deep) 100%);
  }
  .card--back .wordmark {
    position: absolute; left: 150px; top: 150px;
    font-family: 'Play', sans-serif; font-weight: 400;
    font-size: 38px; letter-spacing: 3px;
    color: var(--on-dark);
  }
  .services {
    position: absolute; left: 44px; bottom: 42px;
    font-family: 'Arimo', sans-serif; font-size: 15px;
    color: var(--on-dark); letter-spacing: .3px;
  }
  .services .divider { color: var(--brand-blue); margin: 0 6px; }

  /* Front of card */
  .card--front {
    left: 440px; top: 500px;
    background: var(--paper);
  }
  .card--front .wordmark {
    position: absolute; left: 46px; top: 62px;
    font-family: 'Play', sans-serif; font-weight: 400;
    font-size: 46px; letter-spacing: 3.5px;
    color: var(--ink);
  }
  .person {
    position: absolute; right: 46px; top: 168px; text-align: right;
    font-family: 'Arimo', sans-serif;
  }
  .person__name { font-weight: 700; font-size: 20px; color: var(--ink); }
  .person__role { font-size: 15px; color: var(--brand-blue); margin-top: 3px; }

  .contact {
    position: absolute; left: 46px; bottom: 34px;
    font-family: 'Arimo', sans-serif; font-size: 14px; line-height: 1.45;
    color: var(--muted); list-style: none;
  }
  .contact li { display: flex; align-items: center; gap: 7px; }
  .contact svg { width: 13px; height: 13px; fill: var(--ink); flex: none; }
</style>
</head>
<body>
<main class="canvas">

  <section class="card card--back" aria-label="Card back">
    <div class="wordmark">VARNATH CONSULTING</div>
    <p class="services">Search &amp; Select<span class="divider">|</span>Career<span class="divider">|</span>Coaching<span class="divider">|</span>Leadership<span class="divider">|</span>Outplacement</p>
  </section>

  <section class="card card--front" aria-label="Card front">
    <div class="wordmark">VARNATH CONSULTING</div>

    <div class="person">
      <p class="person__name">Gerald Ashbury</p>
      <p class="person__role">Principal</p>
    </div>

    <ul class="contact">
      <li>PO Box 3917 Tindale Creek</li>
      <li>NSW 2840</li>
      <li>
        <svg viewBox="0 0 16 16" aria-hidden="true"><path d="M3.5 1.5l2.2 2.6-1.2 1.6c.9 2 2.4 3.5 4.3 4.4l1.6-1.2 2.6 2.2-1.3 2.1C6.7 13 3 9.3 1.6 3z"/></svg>
        1300 457 318
      </li>
      <li>
        <svg viewBox="0 0 16 16" aria-hidden="true"><path d="M1 3h14v10H1z M1.8 3.8L8 8.6l6.2-4.8" fill="none" stroke="#1c2e42" stroke-width="1.4"/><path d="M1 3h14L8 8.5z"/></svg>
        jobs@varnathconsulting-example.com
      </li>
      <li>
        <svg viewBox="0 0 16 16" aria-hidden="true"><circle cx="8" cy="8" r="7"/><path d="M1 8h14M8 1c-3 3.5-3 10.5 0 14M8 1c3 3.5 3 10.5 0 14" fill="none" stroke="#fff" stroke-width="1"/></svg>
        www.varnathconsulting-example.com
      </li>
    </ul>
  </section>

</main>
</body>
</html>
```